Business Card Design for Photographer

Updating business card design. Must use included logo. We're a luxury wedding photography business. Elegancy, luxury, consistency are messages we wish to convey.

Visit our website at www.colbyvarnway.com to familiarize yourself more with our brand design currently (fonts, colors etc.). This is what we want to maintain.

Target Market(s)

Luxury Brides and Grooms

Industry/Entity Type

Wedding

Contact Information for Business Card

Current logo (attached to brief)
Name: Colby Varnway
Phone: 5208813047
website/blog
Email

Requirements
Must have
• Current logo (attached to brief)
• Name: Colby Varnway
• Phone: 5208813047
• website/blog
• Email
• Instagram username
Should not have
• bright colors, fonts that don't suit our brand (visit www.colbyvarnway.com)

```html
<!DOCTYPE html>
<html lang="en">
<head>
<meta charset="utf-8">
<title>Colby Varnway Photographers – Business Card</title>
<link rel="stylesheet" href="https://fonts.googleapis.com/css2?family=Tenor+Sans&family=Cormorant+Garamond:wght@500&display=swap">
<style>
  :root {
    --page: #f2f2f0;
    --card-back: #ecebe7;
    --slate: #5d6968;
    --band: rgba(255,255,255,0.55);
    --bloom-blush: #f1b7ad;
    --bloom-white: #eef0ec;
    --bloom-sage: #a9b9ae;
    --bloom-shade: #7d8582;
  }
  * { box-sizing: border-box; margin: 0; padding: 0; }
  html, body { width: 858px; height: 1200px; overflow: hidden; background: var(--page); }
  .canvas { position: relative; width: 858px; height: 1200px; }

  .card { position: absolute; left: 149px; width: 560px; height: 322px; overflow: hidden; }

  /* Front */
  .card--front { top: 137px; }
  .floral-photo {
    position: absolute; inset: 0;
    background:
      radial-gradient(ellipse at 30% 20%, var(--bloom-blush) 0%, transparent 30%),
      radial-gradient(ellipse at 45% 72%, var(--bloom-blush) 0%, transparent 26%),
      radial-gradient(ellipse at 62% 35%, var(--bloom-white) 0%, transparent 45%),
      radial-gradient(ellipse at 20% 60%, var(--bloom-sage) 0%, transparent 35%),
      linear-gradient(90deg, var(--bloom-shade), #b9bcb6 30%, #d9d8d3 60%, var(--bloom-shade));
  }
  .front-band {
    position: absolute; left: 0; right: 0; top: 64px; height: 200px;
    background: var(--band);
  }
  .front-mark {
    position: absolute; left: 50%; top: 64px; transform: translateX(-50%);
    width: 72px; height: 70px; background: var(--slate);
  }
  .front-name {
    position: absolute; left: 0; right: 0; top: 166px; text-align: center;
    font-family: "Tenor Sans", sans-serif; color: var(--slate);
    font-size: 37px; letter-spacing: 5px; line-height: 1;
  }
  .front-tagline {
    position: absolute; left: 0; right: 0; top: 218px; text-align: center;
    font-family: "Tenor Sans", sans-serif; color: var(--slate);
    font-size: 15px; letter-spacing: 7px; line-height: 1;
  }

  /* Back */
  .card--back { top: 631px; background: var(--card-back); }
  .back-mark {
    position: absolute; left: 40px; top: 32px; width: 58px; height: 58px; background: var(--slate);
  }
  .back-name {
    position: absolute; left: 108px; top: 34px;
    font-family: "Tenor Sans", sans-serif; color: var(--slate);
    font-size: 35px; letter-spacing: 4px; line-height: 1;
  }
  .back-tagline {
    position: absolute; left: 112px; top: 76px;
    font-family: "Tenor Sans", sans-serif; color: var(--slate);
    font-size: 16px; letter-spacing: 6.5px; line-height: 1;
  }
  .contact {
    position: absolute; right: 30px; top: 142px; list-style: none;
    font-family: "Cormorant Garamond", serif; font-weight: 500;
    color: #2f3433; font-size: 21px; line-height: 27px; text-align: right;
  }
  .contact li { display: flex; justify-content: flex-end; align-items: center; gap: 10px; }
  .contact .icon { width: 18px; height: 18px; flex: none; }
  .contact .spacer { width: 18px; }
</style>
</head>
<body>
<main class="canvas">

  <section class="card card--front" aria-label="Card front">
    <div class="floral-photo" role="img" aria-label="Photograph of a soft pastel wedding bouquet with blush roses and white blooms"></div>
    <div class="front-band"></div>
    <div class="front-mark"></div>
    <div class="front-name">COLBY VARNWAY</div>
    <div class="front-tagline">PHOTOGRAPHERS</div>
  </section>

  <section class="card card--back" aria-label="Card back">
    <div class="back-mark"></div>
    <div class="back-name">COLBY VARNWAY</div>
    <div class="back-tagline">PHOTOGRAPHERS</div>

    <ul class="contact">
      <li>Colby Varnway <span class="spacer"></span></li>
      <li>(520) 881-3047
        <svg class="icon" viewBox="0 0 18 18" aria-hidden="true"><rect x="5" y="2" width="8" height="14" rx="1.5" fill="none" stroke="#8d9594" stroke-width="1.3"/><line x1="8" y1="13.5" x2="10" y2="13.5" stroke="#8d9594" stroke-width="1.3"/></svg>
      </li>
      <li>www.colbyvarnway.com
        <svg class="icon" viewBox="0 0 18 18" aria-hidden="true"><g fill="none" stroke="#8d9594" stroke-width="1.2"><circle cx="9" cy="9" r="6.5"/><ellipse cx="9" cy="9" rx="3" ry="6.5"/><line x1="2.5" y1="9" x2="15.5" y2="9"/></g></svg>
      </li>
      <li>colby@colbyvarnway.com
        <svg class="icon" viewBox="0 0 18 18" aria-hidden="true"><g fill="none" stroke="#8d9594" stroke-width="1.3"><rect x="2" y="4" width="14" height="10"/><polyline points="2,4 9,10 16,4"/></g></svg>
      </li>
      <li>@colbyvarnwayphoto
        <svg class="icon" viewBox="0 0 18 18" aria-hidden="true"><rect x="3" y="3" width="12" height="12" fill="none" stroke="#8d9594" stroke-width="1.3"/></svg>
      </li>
    </ul>
  </section>

</main>
</body>
</html>
```